Harrow Mobile Servicing and Repairs Van Wrap

Hi Tom,Could you help us design a van wrap to advertise our business?I have attached two examples of vans that we like. We really like the way the Orb Mechanics one has the block of colour towards the back of the van.We also like the way the Ferrel Mechanics one has the logo displayed on the side and think it might work well with our logo. I have attached a blank 'Kovira Tandem' template for your convenience.Some ideas we might like to have included:The slogan "Bringing The Best To You" written on the door with the mobile phone number 0455 903 217 written underneath it (similar to the 'Ferrel' one.)We like the block of colour towards the rear in the ''Orb" design. We like where the logo is placed on the "Ferrel" van.We would like the list of services which we offer written on the van somewhere...maybe in the block of colour if that works well. When listing the services can you exclude QWTR member from the list of services. Please find the list of services on the poster attached which you designed for us.We would also like to have a similar theme to the poster if possible?We do not want to have any photos on the van- just the logo , lists of services, mobile number, web and email addresses.If using colour on the van, can it be vibrant, similar to the blue used in our business card? (attached) These are just ideas, love your work so whatever you think would be best.Thanks,Wendy and Boris

```html
<!DOCTYPE html>
<html lang="en">
<head>
<meta charset="utf-8">
<title>Harrow Mobile Servicing and Repairs – Van Wrap</title>
<link rel="stylesheet" href="https://fonts.googleapis.com/css2?family=Michroma&family=Montserrat:wght@500;700&display=swap">
<style>
  :root{
    --brand-blue:#2b3d8f;
    --brand-navy:#1e2b6b;
    --body-white:#ffffff;
    --outline:#3a3a3a;
    --glass:#e9ecef;
    --trim:#bfc3c7;
    --tyre:#2a2a2a;
    --rim:#9ea3a8;
    --lamp:#c9303a;
    --badge-red:#d21f2b;
    --text-light:#ffffff;
    --text-dark:#1e2b6b;
  }
  *{box-sizing:border-box;margin:0;padding:0}
  html,body{width:1200px;height:717px;overflow:hidden;background:#fff}
  .canvas{position:relative;width:1200px;height:717px;overflow:hidden;background:#fff;font-family:"Michroma",sans-serif;color:var(--text-dark)}
  .view{position:absolute}
  .view svg{position:absolute;left:0;top:0}
  .side-left{left:0;top:0;width:835px;height:360px}
  .side-right{left:0;top:360px;width:835px;height:357px}
  .front{left:835px;top:0;width:365px;height:360px}
  .rear{left:855px;top:370px;width:345px;height:347px}
  .t{position:absolute;white-space:nowrap}
  .centered{text-align:center}
  .phone{font-family:"Montserrat",sans-serif;font-weight:700;color:var(--text-light);display:flex;align-items:center;gap:8px}
  .phone svg{position:static}
  .follow{font-family:"Montserrat",sans-serif;font-weight:500;color:var(--text-light);font-size:8px;text-align:center;line-height:12px}
  .services{list-style:none;color:var(--text-light);font-size:9px;line-height:17px}
  .services li::before{content:"";display:inline-block;width:6px;height:6px;border:1px solid var(--text-light);border-radius:50%;margin-right:6px;vertical-align:middle}
  .brand-mark{display:flex;flex-direction:column;align-items:center;color:var(--text-dark);width:280px}
  .brand-mark .dot{width:70px;height:70px;border-radius:50%;background:var(--brand-navy);margin-bottom:10px}
  .brand-mark .name{font-size:20px;letter-spacing:1px;line-height:1.2}
  .brand-mark .tag{font-size:9.5px;letter-spacing:1.5px;line-height:1.6}
  .mini-mark{display:flex;flex-direction:column;align-items:center;color:var(--text-dark);font-size:7px;text-align:center;line-height:1.35;width:130px}
  .mini-mark .dot{width:26px;height:26px;border-radius:50%;background:var(--brand-navy);margin-bottom:3px}
  .contact-line{font-family:"Montserrat",sans-serif;font-weight:500;font-size:6.5px;color:var(--brand-navy)}
  .slogan{color:var(--text-light);font-size:9px;letter-spacing:1px}
  .model-badge{position:absolute;left:745px;top:352px;display:flex;align-items:center;gap:6px;font-size:14px;color:var(--badge-red);letter-spacing:1px}
  .model-badge .dot{width:14px;height:14px;border-radius:50%;background:var(--badge-red)}
</style>
</head>
<body>
<div class="canvas">

  <section class="view side-left" aria-label="Van side view, front to the left">
    <svg width="835" height="360" viewBox="0 0 835 360">
      <path d="M38,300 L38,175 Q42,130 110,112 L205,30 Q215,16 245,16 L798,16 Q818,16 818,36 L818,290 Q818,305 800,305 L38,305 Z" fill="var(--body-white)" stroke="var(--outline)" stroke-width="1.5"/>
      <path d="M560,16 L800,16 Q818,16 818,36 L818,290 Q818,305 800,305 L540,305 Q600,160 560,16 Z" fill="var(--brand-blue)"/>
      <path d="M230,290 Q260,255 330,255 L818,255 L818,290 Q818,305 800,305 L225,305 Z" fill="var(--brand-blue)"/>
      <path d="M120,112 L210,36 L262,36 L262,112 Z" fill="var(--glass)" stroke="var(--outline)"/>
      <rect x="332" y="165" width="14" height="6" fill="var(--trim)"/>
      <path d="M38,260 L70,260 L70,290 L38,290 Z" fill="var(--trim)"/>
      <rect x="805" y="130" width="13" height="70" fill="var(--lamp)"/>
      <circle cx="150" cy="310" r="58" fill="#fff"/>
      <circle cx="150" cy="310" r="50" fill="var(--tyre)"/>
      <circle cx="150" cy="310" r="30" fill="var(--rim)"/>
      <circle cx="650" cy="310" r="58" fill="#fff"/>
      <circle cx="650" cy="310" r="50" fill="var(--tyre)"/>
      <circle cx="650" cy="310" r="30" fill="var(--rim)"/>
    </svg>
    <div class="t mini-mark" style="left:58px;top:130px"><span class="dot"></span>HARROW MOBILE<br>SERVICING AND REPAIRS</div>
    <div class="t brand-mark" style="left:268px;top:72px"><span class="dot"></span><span class="name">HARROW MOBILE</span><span class="tag">SERVICING AND REPAIRS</span></div>
    <div class="t contact-line centered" style="left:268px;width:280px;top:210px">info@harrowmobile.com.au &nbsp;&nbsp; www.harrowmobile.com.au</div>
    <div class="t slogan centered" style="left:300px;width:240px;top:270px">Bringing the Best to you</div>
    <div class="t phone" style="left:585px;top:44px;font-size:17px">
      <svg width="14" height="14" viewBox="0 0 24 24"><path d="M6.6 10.8a15 15 0 0 0 6.6 6.6l2.2-2.2c.3-.3.7-.4 1-.2 1.1.4 2.3.6 3.6.6.6 0 1 .4 1 1V20c0 .6-.4 1-1 1A17 17 0 0 1 3 4c0-.6.4-1 1-1h3.5c.6 0 1 .4 1 1 0 1.3.2 2.5.6 3.6.1.3 0 .7-.2 1z" fill="#fff"/></svg>0455 903 217</div>
    <div class="t follow" style="left:665px;width:110px;top:70px">Follow us<br>Chatterly · Snapwell</div>
    <ul class="t services" style="left:590px;top:112px">
      <li>Euro Prestige Specialists</li>
      <li>Logbook Servicing</li>
      <li>Transmission Servicing</li>
      <li>Fuel Injection/ Ignition Repairs</li>
      <li>Diagnostics / Fault Finding</li>
      <li>Alternators and Starter Motors</li>
      <li>Genuine/OEM parts used</li>
    </ul>
  </section>

  <section class="view side-right" aria-label="Van side view, front to the right">
    <svg width="835" height="357" viewBox="0 0 835 357">
      <g transform="translate(850,0) scale(-1,1)">
        <path d="M38,300 L38,175 Q42,130 110,112 L205,30 Q215,16 245,16 L798,16 Q818,16 818,36 L818,290 Q818,305 800,305 L38,305 Z" fill="var(--body-white)" stroke="var(--outline)" stroke-width="1.5"/>
        <path d="M560,16 L800,16 Q818,16 818,36 L818,290 Q818,305 800,305 L540,305 Q600,160 560,16 Z" fill="var(--brand-blue)"/>
        <path d="M230,290 Q260,255 330,255 L818,255 L818,290 Q818,305 800,305 L225,305 Z" fill="var(--brand-blue)"/>
        <path d="M120,112 L210,36 L262,36 L262,112 Z" fill="var(--glass)" stroke="var(--outline)"/>
        <path d="M38,260 L70,260 L70,290 L38,290 Z" fill="var(--trim)"/>
        <rect x="805" y="130" width="13" height="70" fill="var(--lamp)"/>
        <circle cx="150" cy="310" r="58" fill="#fff"/>
        <circle cx="150" cy="310" r="50" fill="var(--tyre)"/>
        <circle cx="150" cy="310" r="30" fill="var(--rim)"/>
        <circle cx="650" cy="310" r="58" fill="#fff"/>
        <circle cx="650" cy="310" r="50" fill="var(--tyre)"/>
        <circle cx="650" cy="310" r="30" fill="var(--rim)"/>
      </g>
    </svg>
    <div class="t phone" style="left:55px;top:48px;font-size:17px">
      <svg width="14" height="14" viewBox="0 0 24 24"><path d="M6.6 10.8a15 15 0 0 0 6.6 6.6l2.2-2.2c.3-.3.7-.4 1-.2 1.1.4 2.3.6 3.6.6.6 0 1 .4 1 1V20c0 .6-.4 1-1 1A17 17 0 0 1 3 4c0-.6.4-1 1-1h3.5c.6 0 1 .4 1 1 0 1.3.2 2.5.6 3.6.1.3 0 .7-.2 1z" fill="#fff"/></svg>0455 903 217</div>
    <div class="t follow" style="left:130px;width:110px;top:74px">Follow us<br>Chatterly · Snapwell</div>
    <ul class="t services" style="left:52px;top:114px">
      <li>Euro Prestige Specialists</li>
      <li>Logbook Servicing</li>
      <li>Transmission Servicing</li>
      <li>Fuel Injection/ Ignition Repairs</li>
      <li>Diagnostics / Fault Finding</li>
      <li>Alternators and Starter Motors</li>
      <li>Genuine/OEM parts used</li>
    </ul>
    <div class="t brand-mark" style="left:330px;top:60px"><span class="dot"></span><span class="name">HARROW MOBILE</span><span class="tag">SERVICING AND REPAIRS</span></div>
    <div class="t contact-line centered" style="left:330px;width:280px;top:198px">info@harrowmobile.com.au &nbsp;&nbsp; www.harrowmobile.com.au</div>
    <div class="t mini-mark" style="left:630px;top:150px"><span class="dot"></span>HARROW MOBILE<br>SERVICING AND REPAIRS</div>
    <div class="t slogan centered" style="left:300px;width:240px;top:270px">Bringing the Best to you</div>
  </section>

  <div class="model-badge"><span class="dot"></span>KOVIRA</div>

  <section class="view front" aria-label="Van front view">
    <svg width="365" height="360" viewBox="0 0 365 360">
      <path d="M55,330 L50,140 Q52,90 80,25 Q90,12 110,12 L255,12 Q275,12 285,25 Q313,90 315,140 L310,330 Z" fill="var(--body-white)" stroke="var(--outline)" stroke-width="1.5"/>
      <path d="M85,105 Q92,55 110,30 L255,30 Q273,55 280,105 Z" fill="var(--glass)" stroke="var(--outline)"/>
      <rect x="55" y="180" width="60" height="28" rx="6" fill="var(--trim)" stroke="var(--outline)"/>
      <rect x="250" y="180" width="60" height="28" rx="6" fill="var(--trim)" stroke="var(--outline)"/>
      <rect x="120" y="182" width="125" height="34" rx="4" fill="var(--trim)" stroke="var(--outline)"/>
      <rect x="50" y="245" width="265" height="40" rx="8" fill="#d6d9dc" stroke="var(--outline)"/>
      <rect x="140" y="255" width="85" height="20" fill="#fff" stroke="var(--outline)"/>
      <rect x="55" y="295" width="40" height="50" rx="6" fill="var(--tyre)"/>
      <rect x="270" y="295" width="40" height="50" rx="6" fill="var(--tyre)"/>
    </svg>
    <div class="t" style="left:116px;top:120px;width:20px;height:20px;border-radius:50%;background:var(--brand-navy)"></div>
    <div class="t" style="left:142px;top:124px;font-size:10px;color:var(--text-dark)">HARROW MOBILE</div>
    <div class="t" style="left:142px;top:140px;font-size:6px;color:var(--text-dark);letter-spacing:1px">SERVICING AND REPAIRS</div>
  </section>

  <section class="view rear" aria-label="Van rear view">
    <svg width="345" height="347" viewBox="0 0 345 347">
      <path d="M30,320 L30,60 Q32,20 60,10 L290,10 Q318,20 320,60 L320,320 Z" fill="var(--brand-blue)" stroke="var(--outline)" stroke-width="1.5"/>
      <path d="M55,120 L58,45 Q62,28 80,28 L270,28 Q288,28 292,45 L295,120 Z" fill="none" stroke="#5a6bb0"/>
      <rect x="30" y="90" width="14" height="80" fill="var(--lamp)"/>
      <rect x="306" y="90" width="14" height="80" fill="var(--lamp)"/>
      <rect x="30" y="275" width="290" height="30" fill="var(--brand-navy)"/>
      <rect x="135" y="280" width="80" height="20" fill="#fff" stroke="var(--outline)"/>
      <rect x="40" y="305" width="40" height="40" rx="6" fill="var(--tyre)"/>
      <rect x="270" y="305" width="40" height="40" rx="6" fill="var(--tyre)"/>
    </svg>
    <div class="t" style="left:158px;top:52px;width:34px;height:34px;border-radius:50%;background:#fff"></div>
    <div class="t centered" style="left:30px;width:290px;top:94px;font-size:12px;color:var(--text-light)">HARROW MOBILE</div>
    <div class="t centered" style="left:30px;width:290px;top:112px;font-size:6.5px;color:var(--text-light);letter-spacing:1px">SERVICING AND REPAIRS</div>
    <div class="t phone" style="left:30px;width:290px;justify-content:center;top:138px;font-size:14px">
      <svg width="11" height="11" viewBox="0 0 24 24"><path d="M6.6 10.8a15 15 0 0 0 6.6 6.6l2.2-2.2c.3-.3.7-.4 1-.2 1.1.4 2.3.6 3.6.6.6 0 1 .4 1 1V20c0 .6-.4 1-1 1A17 17 0 0 1 3 4c0-.6.4-1 1-1h3.5c.6 0 1 .4 1 1 0 1.3.2 2.5.6 3.6.1.3 0 .7-.2 1z" fill="#fff"/></svg>0455 903 217</div>
    <div class="t contact-line centered" style="left:30px;width:290px;top:164px;color:var(--text-light);font-size:6px">info@harrowmobile.com.au &nbsp; www.harrowmobile.com.au</div>
    <div class="t slogan centered" style="left:30px;width:290px;top:252px;font-size:8px">Bringing the Best to you</div>
  </section>

</div>
</body>
</html>
```